Solar Ad for direct mail campaign designed to grab attention

My company is doing a direct mail campaign on a 6.25-9in flyer. There will be wording on it, but I need a picture to grab attention. I need a picture of a pink unicorn made out of solar panels fighting a pirate ship with power lines and electrical wires on it in a battle of the galaxy scene. I want to make it look like a mystical solar creature is saving the planet from the "power pirates" AKA power company. Please be over-the-top and creative.

Target Market(s)

30-55 year old homeowners

Industry/Entity Type

Solar Energy

Font styles to use
Sans Serif

Colors
876aae
b768aa
e667a6
fece3e
33b8a4
3176b5

Requirements
Must have
• Lots of Color, exxagertion and creativity
Nice to have
• I want the unicorn to be the largest thing on the picture, with a picture of the earth in the backround. The pirate ship must be battling with the unicorn. The pirate ship must have power lines on it, and the pirates must have on yellow hard hats to show that they represent the power company
Should not have
• no rainbows

```html
<!DOCTYPE html>
<html lang="en">
<head>
<meta charset="utf-8">
<title>Save the Universe with Solar – Direct Mail Flyer</title>
<link href="https://fonts.googleapis.com/css2?family=Lato:ital,wght@0,400;0,700;0,900;1,700;1,900&display=swap" rel="stylesheet">
<style>
  :root {
    --stage: #16181c;
    --ink: #1d1d22;
    --body-ink: #3a3a40;
    --magenta: #c4137a;
    --magenta-deep: #8e0c55;
    --band: #d457a0;
    --paper-top: #d9d9dc;
    --paper-bottom: #ffffff;
    --white: #ffffff;
  }
  * { box-sizing: border-box; margin: 0; padding: 0; }
  html, body { width: 1200px; height: 848px; overflow: hidden; }
  body {
    background: var(--stage);
    font-family: "Lato", Arial, sans-serif;
    position: relative;
  }
  .flyer {
    position: absolute;
    left: 322px;
    top: 24px;
    width: 556px;
    height: 800px;
    overflow: hidden;
    background: linear-gradient(180deg, var(--paper-top) 0%, var(--paper-bottom) 70%);
  }
  .flyer-art { position: absolute; inset: 0; width: 556px; height: 800px; }
  .headline {
    position: absolute;
    top: 44px;
    left: 0;
    width: 100%;
    text-align: center;
    color: var(--white);
    font-weight: 900;
    font-size: 42px;
    line-height: 1.05;
    letter-spacing: 1px;
    text-transform: uppercase;
  }
  .hook {
    position: absolute;
    left: 30px;
    top: 376px;
    width: 236px;
    font-weight: 900;
    font-size: 21px;
    line-height: 1.2;
    color: var(--ink);
  }
  .hook strong { display: block; font-size: 22px; }
  .story {
    position: absolute;
    left: 30px;
    top: 522px;
    width: 245px;
    font-size: 10.5px;
    line-height: 1.35;
    color: var(--body-ink);
  }
  .story p { margin-bottom: 6px; }
  .source { color: var(--magenta); font-weight: 900; font-size: 11px; margin-bottom: 2px !important; }
  .benefits {
    position: absolute;
    left: 292px;
    top: 490px;
    width: 244px;
    font-size: 9.5px;
    line-height: 1.28;
    color: var(--body-ink);
  }
  .benefits p { margin-bottom: 5px; }
  .quote { font-weight: 900; font-style: italic; font-size: 10.5px; color: var(--ink); }
  .shout { text-transform: uppercase; }
  .offer-band {
    position: absolute;
    left: 0;
    bottom: 0;
    width: 100%;
    height: 76px;
    background: var(--band);
    color: var(--white);
    text-align: center;
    text-transform: uppercase;
    font-size: 17px;
    line-height: 1.25;
    padding-top: 16px;
    letter-spacing: 0.5px;
  }
</style>
</head>
<body>
  <main class="flyer">
    <svg class="flyer-art" viewBox="0 0 556 800">
      <defs>
        <linearGradient id="cosmos" x1="0" y1="0" x2="0.6" y2="1">
          <stop offset="0" stop-color="#2a0216"/>
          <stop offset="0.35" stop-color="#7a0a48"/>
          <stop offset="0.7" stop-color="#d21f8c"/>
          <stop offset="1" stop-color="#5a0634"/>
        </linearGradient>
        <radialGradient id="glow" cx="0.55" cy="0.6" r="0.45">
          <stop offset="0" stop-color="#f3a4d4" stop-opacity="0.7"/>
          <stop offset="1" stop-color="#f3a4d4" stop-opacity="0"/>
        </radialGradient>
      </defs>
      <g role="img" aria-label="Illustration: a pink unicorn made of solar panels battles a pirate ship strung with power lines above a glowing planet in space">
        <path d="M0 0H556V450C420 440 260 330 0 230Z" fill="url(#cosmos)"/>
        <path d="M0 0H556V450C420 440 260 330 0 230Z" fill="url(#glow)"/>
      </g>
      <path class="swoosh" d="M0 230C260 330 420 440 556 450V474C420 464 260 354 0 252Z" fill="var(--magenta-deep)"/>
      <path class="swoosh-accent" d="M0 266C100 286 180 316 240 346C170 318 90 292 0 278Z" fill="var(--magenta)"/>
    </svg>

    <h1 class="headline">Save the Universe<br>with Solar!</h1>

    <h2 class="hook">Would you go Solar if it was cheaper than electricity? If you answered yes, <strong>KEEP READING</strong></h2>

    <section class="story">
      <p class="source">According to sunfacts.org</p>
      <p>“Solar is the most abundant energy resource on earth”</p>
      <p>Here’s what we want you to do: Look up electricity rate increases from the past ten, and twenty years and ask yourself if you want to wait around for the same increases for the future…</p>
      <p>When we first began installing solar, our customers were worried that this was “too good to be true”. But after their first year of having solar, their only regret was that they didn’t call us sooner!</p>
    </section>

    <section class="benefits">
      <p>Solar has become the cheaper option. Not only does it cost nothing to install, but it puts money back in your pocket day one! How would you like to know that you will never have to worry about another price increase from the power company, EVER?</p>
      <p class="quote">Solar is amazing! If you can pay for a light bill, you can pay for solar!” -Dana Whitfield</p>
      <p class="shout">Doesn’t it bother you that the power companies are going to keep increasing the price for no real reason at all? Most of all, aren’t you nauseated by the fact that you will never cease paying for your electrical bill?! Solar is that answer! No out of pocket costs. Savings day one. Increased property value. Owning your power rather than getting the power companies richer!</p>
    </section>

    <footer class="offer-band">
      See if your home qualifies for free!<br>
      Now through Frbruary 15th! Call now! ##########
    </footer>
  </main>
</body>
</html>
```